Branded PowerPoint Template Design

Would like a general PowerPoint template customized with my company branding to use in presentations for customers. The company is a talent management consulting and recruiting company called Brenwick & Associates. I would like a design that incorporates the logo colors with a clean and simple look.
Target Market(s)
Slides are typically viewed by HR and Corporate executives either briefing our capabilities or delivering solution results.
Industry/Entity Type
It Company
Requirements
Must have
- Simple clean design that will not draw attention away from the actual presentation. Design should go well with the logo branding and colors.
Should not have
- Should not have any pictures of people

```html
<!DOCTYPE html>
<html lang="en">
<head>
<meta charset="utf-8">
<title>Brenwick &amp; Associates – Slide Template</title>
<link rel="stylesheet" href="https://fonts.googleapis.com/css2?family=Roboto+Condensed:wght@700&family=Roboto:wght@400;500;700&display=swap">
<style>
  :root {
    --navy: #1c1160;
    --cyan: #1fb8dc;
    --text: #4a4a4a;
    --white: #ffffff;
    --footer: #9b9ca0;
    --page: #ffffff;
  }
  * { margin: 0; padding: 0; box-sizing: border-box; }
  html, body { width: 1200px; height: 900px; overflow: hidden; background: var(--page); }
  .slide { position: relative; width: 1200px; height: 900px; background: var(--page); font-family: "Roboto", Arial, sans-serif; }

  .slide-header { position: absolute; left: 0; top: 0; width: 1200px; height: 123px; background: var(--navy); }
  .slide-title { position: absolute; left: 30px; top: 24px; font-family: "Roboto Condensed", "Arial Narrow", sans-serif; font-weight: 700; font-size: 56px; line-height: 66px; color: var(--white); letter-spacing: 0.5px; }
  .brand-name { position: absolute; right: 28px; top: 42px; font-family: "Roboto Condensed", "Arial Narrow", sans-serif; font-weight: 700; font-size: 32px; line-height: 40px; color: var(--white); }

  .intro { position: absolute; left: 86px; top: 190px; width: 1060px; }
  .intro-heading { font-weight: 700; font-size: 23px; line-height: 30px; color: var(--navy); margin-bottom: 6px; }
  .intro-text { font-size: 17.5px; line-height: 30px; color: var(--text); }

  .profile-photo { position: absolute; left: 75px; top: 426px; width: 336px; height: 336px; border-radius: 50%; border: 7px solid var(--navy); background: radial-gradient(circle at 50% 40%, #d9d9d9 0%, #9a9a9a 55%, #4a4a4a 100%); }

  .contact-card { position: absolute; left: 443px; top: 370px; width: 337px; height: 214px; background: var(--cyan); padding: 43px 0 0 28px; color: var(--white); }
  .contact-name { font-weight: 700; font-size: 21px; line-height: 26px; margin-bottom: 14px; }
  .contact-list { list-style: none; padding-left: 15px; }
  .contact-list li { display: flex; align-items: center; font-size: 13px; line-height: 24.5px; }
  .contact-dot { width: 8px; height: 8px; border-radius: 50%; background: var(--white); margin-right: 15px; }

  .building-photo { position: absolute; left: 443px; top: 604px; width: 337px; height: 196px; background: linear-gradient(135deg, #cfe6f7 0%, #6fa8dc 40%, #2a5fa8 75%, #1b3f78 100%); }

  .summary-panel { position: absolute; left: 801px; top: 369px; width: 341px; height: 431px; background: var(--navy); padding: 25px 26px 0 30px; }
  .summary-text { font-size: 17.5px; line-height: 33px; color: var(--white); }

  .slide-footer { position: absolute; left: 0; bottom: 0; width: 1200px; height: 42px; background: var(--footer); }
</style>
</head>
<body>
<main class="slide">
  <header class="slide-header">
    <h1 class="slide-title">Project Title Here</h1>
    <div class="brand-name">Brenwick &amp; Associates</div>
  </header>

  <section class="intro">
    <h2 class="intro-heading">Bullet Title Heading Here Bullet Title Heading Here</h2>
    <p class="intro-text">Lorem ipsum dolor sit Lorem ipsum dolor sit&nbsp; Lorem ipsum dolor sit Lorem ipsum dolor sit&nbsp; Lorem ipsum dolor sit Lorem ipsum dolor sit&nbsp; Lorem ipsum dolor sit Lorem ipsum dolor sit&nbsp; Lorem ipsum dolor sit Lorem ipsum dolor sit&nbsp; Lorem ipsum dolor sit Lorem ipsum dolor sit&nbsp; Lorem ipsum dolor sit Lorem ipsum dolor sit&nbsp; Lorem ipsum dolor sit Lorem ipsum dolor sit</p>
  </section>

  <div class="profile-photo" role="img" aria-label="Portrait photo of the company CEO"></div>

  <section class="contact-card">
    <h3 class="contact-name">Company CEO Name</h3>
    <ul class="contact-list">
      <li><span class="contact-dot"></span>Mrs.ellaroe@social</li>
      <li><span class="contact-dot"></span>Mrs.ellaroe@mailbox.net</li>
      <li><span class="contact-dot"></span>Mrs.ellaroe@video</li>
      <li><span class="contact-dot"></span>Mrs.ellaroe@network</li>
    </ul>
  </section>

  <div class="building-photo" role="img" aria-label="Photo of a glass office tower against a blue sky"></div>

  <section class="summary-panel">
    <p class="summary-text">Lorem ipsum dolor sit Lorem ipsum dolor sit&nbsp; Lorem ipsum dolor sit Lorem ipsum dolor sit&nbsp; Lorem ipsum dolor sit Lorem ipsum dolor sit&nbsp; Lorem ipsum dolor sit Lorem ipsum dolor sit&nbsp; Lorem ipsum dolor sit Lorem ipsum dolor sit&nbsp; Lorem ipsum dolor sit Lorem ipsum dolor sit&nbsp; Lorem ipsum dolor sit Lorem ipsum dolor sit</p>
  </section>

  <footer class="slide-footer"></footer>
</main>
</body>
</html>
```